"Cork Hollow Excursions" is a top notch Santa Barbara County Wine Tour company.

We provide scenic, boutique and custom wine tours. I need the card to be clean and classy. I will provide our logo. I would like the logo to cover the back side of the card as an option and would like to see a couple color options other then our signature green and gold. I would like to see some creative options and let the designers come up with options.
I need cards for myself and my team. The final design should communicate "An authentic and boutique wine tour experience"
Please use my website for reference www.corkhollowexcursions.com

Target Market(s)

We have a wide range of clients from millennials to baby boomers

Industry/Entity Type

Tour

Contact Information for Business Card

Contact info:
Dale Munford
805-291-6384
info@corkhollowexcursions.com
corkhollowexcursions.com

Colors

Designer to choose colors to be used in the design.

Requirements
Must have
• my logo
Nice to have
• *I would like to have the backside side with the logo and the company statement
• "An authentic and boutique wine tour experience" as an option.
• *I would also like to see what the designers can create!
• *I would like to see an option that incorporates or social: snapgrid, rovia, route scout
Should not have
• I do not want it too busy.

```html
<!DOCTYPE html>
<html lang="en">
<head>
<meta charset="utf-8">
<title>Cork Hollow Excursions — Business Card</title>
<link rel="stylesheet" href="https://fonts.googleapis.com/css2?family=Cinzel:wght@500&family=EB+Garamond:wght@400&display=swap">
<style>
  :root {
    --canvas: #2b2b2d;
    --card-green: #2a6a46;
    --card-white: #ffffff;
    --ink-green: #2e6b47;
    --ink-copper: #b3866a;
    --ink-dark: #2a2a2a;
    --on-green: #f4f1ea;
  }
  * { box-sizing: border-box; margin: 0; padding: 0; }
  html, body { width: 1200px; height: 880px; overflow: hidden; }
  body { background: var(--canvas); position: relative; font-family: "EB Garamond", Georgia, serif; }

  .card {
    position: absolute;
    width: 660px;
    height: 378px;
    border-radius: 22px;
    overflow: hidden;
  }

  /* Back side */
  .card-back { left: 60px; top: 50px; background: var(--card-green); color: var(--on-green); }
  .card-back .brand-name {
    position: absolute; left: 0; right: 0; top: 130px;
    text-align: center;
    font-family: "Cinzel", "Times New Roman", serif;
    font-weight: 500; font-size: 34px; letter-spacing: 2px;
  }
  .card-back .tagline {
    position: absolute; left: 0; right: 0; top: 272px;
    text-align: center; font-size: 22px; letter-spacing: 3px;
  }

  /* Front side */
  .card-front { left: 480px; top: 452px; background: var(--card-white); }
  .card-front .brand-name {
    position: absolute; right: 46px; top: 58px;
    font-family: "Cinzel", "Times New Roman", serif;
    font-weight: 500; font-size: 24px; letter-spacing: 1.5px;
    color: var(--ink-green);
  }
  .card-front .rule {
    position: absolute; left: 60px; right: 46px; top: 160px;
    height: 1px; background: var(--ink-green);
  }
  .socials { position: absolute; right: 46px; top: 178px; display: flex; gap: 12px; }
  .socials .badge {
    width: 32px; height: 32px; border-radius: 50%;
    border: 3px solid var(--ink-green);
  }
  .person {
    position: absolute; left: 60px; top: 218px;
    font-family: "Cinzel", "Times New Roman", serif;
    font-size: 24px; letter-spacing: 1px; color: var(--ink-copper);
  }
  .contacts { position: absolute; left: 60px; top: 262px; list-style: none; }
  .contacts li {
    display: flex; align-items: center; gap: 8px;
    font-size: 19px; color: var(--ink-dark); line-height: 30px;
  }
  .contacts svg { width: 20px; height: 20px; flex: none; }
</style>
</head>
<body>

<section class="card card-back" aria-label="Card back">
  <div class="brand-name">Cork Hollow Excursions</div>
  <p class="tagline">An authentic and boutique wine tour experience</p>
</section>

<section class="card card-front" aria-label="Card front">
  <div class="brand-name">Cork Hollow Excursions</div>
  <div class="rule"></div>
  <div class="socials">
    <span class="badge" role="img" aria-label="route scout"></span>
    <span class="badge" role="img" aria-label="snapgrid"></span>
    <span class="badge" role="img" aria-label="rovia"></span>
  </div>
  <div class="person">Dale Munford</div>
  <ul class="contacts">
    <li>
      <svg viewBox="0 0 20 20" aria-hidden="true"><circle cx="10" cy="10" r="10" fill="#2e6b47"/><path d="M6.5 5.5l2 0 1 2.5-1.3 1a6 6 0 0 0 2.8 2.8l1-1.3 2.5 1v2a1 1 0 0 1-1 1A8 8 0 0 1 5.5 6.5a1 1 0 0 1 1-1z" fill="#fff"/></svg>
      805-291-6384
    </li>
    <li>
      <svg viewBox="0 0 20 20" aria-hidden="true"><circle cx="10" cy="10" r="10" fill="#2e6b47"/><rect x="5" y="6.5" width="10" height="7" fill="none" stroke="#fff" stroke-width="1.2"/><path d="M5 6.5l5 4 5-4" fill="none" stroke="#fff" stroke-width="1.2"/></svg>
      info@corkhollowexcursions.com
    </li>
    <li>
      <svg viewBox="0 0 20 20" aria-hidden="true"><circle cx="10" cy="10" r="10" fill="#2e6b47"/><circle cx="10" cy="10" r="5" fill="none" stroke="#fff" stroke-width="1.2"/><path d="M5 10h10M10 5c-2.5 3-2.5 7 0 10M10 5c2.5 3 2.5 7 0 10" fill="none" stroke="#fff" stroke-width="1"/></svg>
      corkhollowexcursions.com
    </li>
  </ul>
</section>

</body>
</html>
```